Varrowick Biomedical Research Institute (VBRI) Web Design

VBRI is a non-profit organization focused on saving the lives of terminally ill patients by becoming the leaders in cutting-edge research, innovative technologies, utilizing national and international partnerships as well as the associated allopathic and naturopathic treatments necessary to do so.

Our primary focus is raising funds to support the research and acquisition of new technologies for life saving treatments which are NOT a one size fits all approach like conventional medicine but rather a marriage of the latest technologies used in combination with other new treatment possibilities for a successful end result.

Our domain is varrowickbr.org

Logo files are attached.

Looking for something clean, light, healthy.

Target Market(s)

The site should look and feel towards research/scientific grant writing.
Medical professionals, Medical Scientists.

Industry/Entity Type

Medical And Science

Number of Pages Required

4 page

Requirements
Nice to have
• Here are examples of sites I like in the order of how much I like them.
• https://www.palvenhope.org/give.html
• https://www.thekqtf.org/donate-to-kqtf
• https://www.curewaveinst.org/we-are-cwi/join-the-cause
• https://www.healquest.org/involved/donate.html
• https://give.nptf.org/checkout/donation?eid=58217
• https://www.moravind.org/how-you-can-help
• https://donate3.healquest.org/

```html
<!DOCTYPE html>
<html lang="en">
<head>
<meta charset="utf-8">
<title>Varrowick Biomedical Research Institute</title>
<link href="https://fonts.googleapis.com/css2?family=Montserrat:wght@400;600;700&family=Open+Sans:wght@400;600;700&display=swap" rel="stylesheet">
<style>
:root{
  --green:#3f9a3a;
  --green-dark:#2f7f2c;
  --blue:#1b72b8;
  --blue-dark:#135d99;
  --teal:#1a86b4;
  --ink:#2b2b2b;
  --muted:#6a6a6a;
  --paper:#ffffff;
  --mist:#eef1f4;
  --nav:#f2f2f2;
  --footer:#1b1b1b;
  --footer-text:#9a9a9a;
}
*{box-sizing:border-box;margin:0;padding:0}
html,body{width:1200px;height:3644px;overflow:hidden}
body{font-family:"Open Sans",Arial,sans-serif;color:var(--ink);background:var(--paper);position:relative}
a{color:inherit;text-decoration:none}

/* header */
.site-header{height:97px;position:relative;background:var(--paper)}
.brand{position:absolute;left:151px;top:30px;display:flex;align-items:center;gap:12px}
.brand-mark{width:34px;height:34px;border-radius:50%;background:var(--green)}
.brand-name{font-family:"Montserrat",sans-serif;font-weight:700;color:var(--blue);font-size:17px;white-space:nowrap}
.header-actions{position:absolute;right:146px;top:29px;display:flex;gap:10px}
.btn{display:inline-flex;align-items:center;justify-content:center;font-family:"Montserrat",sans-serif;font-weight:600;font-size:13px;color:#fff;border-radius:2px;white-space:nowrap}
.btn-blue{background:var(--blue);width:148px;height:44px}
.btn-green{background:var(--green);width:128px;height:44px}

.main-nav{height:49px;background:var(--nav);border-top:1px solid #e2e2e2;border-bottom:1px solid #e2e2e2;position:relative}
.main-nav ul{list-style:none;display:flex;position:absolute;left:151px;top:0;height:47px}
.main-nav li{width:118px;display:flex;align-items:center;justify-content:center;font-size:13px;color:#444;border-left:1px solid #dcdcdc;white-space:nowrap}
.main-nav li:last-child{border-right:1px solid #dcdcdc}
.search-btn{position:absolute;right:146px;top:-1px;width:73px;height:49px;background:#3a3a3a;display:flex;align-items:center;justify-content:center}

/* hero */
.hero{height:588px;position:relative;background:linear-gradient(100deg,#c8ccd0 0%,#a9b4be 30%,#4e6f93 55%,#8a6a58 78%,#caa58c 100%)}
.hero-card{position:absolute;left:0;top:170px;width:506px;height:287px;background:rgba(255,255,255,.88);border-radius:0 6px 6px 0;padding:36px 0 0 151px}
.hero-card h1{font-family:"Montserrat",sans-serif;font-size:21px;font-weight:700;color:#222}
.hero-card p{font-size:13px;line-height:20px;color:#555;margin-top:22px;width:310px}
.hero-card .actions{display:flex;gap:8px;margin-top:32px}
.btn-outline{width:134px;height:42px;border:1px solid #9a9a9a;color:#444;background:#fff}
.btn-hero{width:136px;height:42px}

.pillars{height:92px;background:var(--blue);display:flex;justify-content:center;align-items:center;gap:70px;color:#fff}
.pillar{display:flex;align-items:center;gap:12px;font-size:18px}
.pillar b{font-weight:700}
.pillar-icon{width:40px;height:40px;border-radius:50%;border:1px solid rgba(255,255,255,.5);display:flex;align-items:center;justify-content:center}

/* sections */
.section-title{text-align:center;font-family:"Montserrat",sans-serif;font-weight:700;font-size:34px;color:var(--teal);text-transform:uppercase}
.divider{display:block;margin:18px auto 0}

.donate{height:790px;background:var(--mist);position:relative;padding-top:96px}
.section-mark{width:44px;height:44px;border-radius:50%;background:var(--green);margin:0 auto 18px}
.card-row{position:absolute;left:151px;display:flex;gap:39px}
.card{width:274px;height:335px;background:var(--paper);border-radius:6px;box-shadow:0 2px 6px rgba(0,0,0,.12);position:relative;text-align:center}
.card-media{height:168px;border-radius:6px 6px 0 0}
.card h3{font-family:"Montserrat",sans-serif;font-size:16px;font-weight:600;color:#222;margin-top:18px}
.card .rule{width:52px;height:2px;background:var(--green);margin:10px auto 0}
.card p{font-size:11.5px;line-height:17px;color:#666;padding:0 26px;margin-top:14px}
.card-go{position:absolute;left:50%;bottom:-2px;transform:translate(-50%,0);width:38px;height:38px;border-radius:50%;background:#fff;box-shadow:0 1px 4px rgba(0,0,0,.2);display:flex;align-items:center;justify-content:center}
.see-more{position:absolute;left:515px;top:690px;width:172px;height:40px;background:var(--green);font-size:12px}

.treatment{height:457px;display:flex}
.treatment-media{width:556px;height:457px;background:linear-gradient(135deg,#e9ecef 0%,#cfd6dc 45%,#3d5fa8 70%,#e2e5e8 100%)}
.treatment-body{padding:70px 0 0 50px;width:600px}
.treatment-body h2{font-family:"Montserrat",sans-serif;font-size:30px;font-weight:700;color:var(--teal);white-space:nowrap}
.treatment-body h4{font-size:14px;font-weight:700;color:#555;margin-top:6px;white-space:nowrap}
.treatment-body p{font-size:12px;line-height:20px;color:#666;margin-top:44px;width:445px}
.btn-read{width:132px;height:40px;background:var(--green);font-size:12px;margin-top:40px}

.monthly{height:445px;background:linear-gradient(100deg,#3a9a3e 0%,#2c8a6a 45%,#1a69a8 100%);color:#fff;text-align:center;padding-top:84px}
.monthly h2{font-family:"Montserrat",sans-serif;font-size:30px;font-weight:700}
.monthly p{width:760px;margin:40px auto 0;font-size:12.5px;line-height:22px}
.btn-ghost{width:142px;height:40px;border:1px solid rgba(255,255,255,.8);font-size:12px;margin-top:42px}

.interest{height:646px;background:var(--mist);position:relative;padding-top:80px}
.interest .card-row{top:216px}
.slider-arrow{position:absolute;top:372px;width:26px;height:26px;background:#2b2b2b;display:flex;align-items:center;justify-content:center}

.cta-band{height:131px;background:var(--green);display:flex;justify-content:center;align-items:center;gap:42px}
.cta{width:274px;height:50px;background:#1e3b1d;display:flex;align-items:center;color:#fff;font-size:14px;font-weight:600;border-radius:2px}
.cta-icon{width:50px;height:50px;flex:none;background:var(--blue);display:flex;align-items:center;justify-content:center;margin-right:16px;border-radius:2px 0 0 2px}
.cta-label{flex:1;white-space:nowrap}
.cta .arrow{flex:none;margin-right:16px}

.site-footer{height:349px;background:var(--footer);position:relative;color:var(--footer-text)}
.footer-col{position:absolute;top:45px}
.footer-col h5{font-family:"Montserrat",sans-serif;font-size:17px;font-weight:700;color:#fff;text-transform:uppercase;margin-bottom:22px}
.contact-col{left:151px;font-size:12px;line-height:18px}
.contact-col .org{color:#ccc}
.contact-col .line{font-size:17px;line-height:30px;color:#bbb;display:flex;align-items:center;gap:6px}
.nav-col{left:537px;font-size:12px;line-height:21px}
.nav-col li{list-style:none}
.nav-col li:first-child{color:var(--green)}
.sub-col{left:818px}
.sub-field{width:236px;height:38px;background:#2a2a2a;display:flex;align-items:center;justify-content:space-between;padding:0 14px;font-size:12px;color:#777}
.socials{display:flex;gap:10px;margin-top:26px}
.socials span{width:30px;height:30px;border-radius:50%;border:1px solid #555}
.copyright{position:absolute;left:0;right:0;bottom:22px;text-align:center;font-size:11px;color:#666}
</style>
</head>
<body>

<header class="site-header">
  <a class="brand" href="#"><span class="brand-mark"></span><span class="brand-name">Varrowick Biomedical Research Institute</span></a>
  <div class="header-actions">
    <a class="btn btn-blue" href="#">Patient Referrals</a>
    <a class="btn btn-green" href="#">Donate Now</a>
  </div>
</header>

<nav class="main-nav">
  <ul>
    <li>About Us</li><li>Care &amp; Treatment</li><li>Research</li><li>Training</li><li>Get Involved</li><li>Contact Us</li>
  </ul>
  <div class="search-btn">
    <svg width="20" height="20" viewBox="0 0 20 20"><circle cx="8" cy="8" r="6" fill="none" stroke="#fff" stroke-width="2"/><line x1="12.5" y1="12.5" x2="18" y2="18" stroke="#fff" stroke-width="2"/></svg>
  </div>
</nav>

<section class="hero" role="img" aria-label="Photo of a smiling young patient in a blue head scarf with his smiling mother">
  <div class="hero-card">
    <h1>Some Headline Goes Here...</h1>
    <p>Lorem ipsum dolor sit amet, consectetur adipisicing elit, sed do eiusmod tempor incididunt ut labore et nostrud exercitation ullamco laboris.</p>
    <div class="actions">
      <a class="btn btn-green btn-hero" href="#">Donate Now</a>
      <a class="btn btn-outline" href="#">Know More</a>
    </div>
  </div>
</section>

<section class="pillars">
  <div class="pillar"><span class="pillar-icon"><svg width="18" height="18" viewBox="0 0 18 18"><path d="M4 16 L10 4 L14 8" fill="none" stroke="#fff" stroke-width="1.6"/></svg></span><span><b>Cutting-Edge</b> Research</span></div>
  <div class="pillar"><span class="pillar-icon"><svg width="18" height="18" viewBox="0 0 18 18"><path d="M7 2 V8 L3 15 H15 L11 8 V2" fill="none" stroke="#fff" stroke-width="1.6"/></svg></span><span><b>Innovative</b> Technologies</span></div>
  <div class="pillar"><span class="pillar-icon"><svg width="18" height="18" viewBox="0 0 18 18"><circle cx="9" cy="9" r="3" fill="none" stroke="#fff" stroke-width="1.6"/><circle cx="9" cy="9" r="7" fill="none" stroke="#fff" stroke-width="1.2" stroke-dasharray="3 2"/></svg></span><span><b>Renowned</b> Partners</span></div>
</section>

<section class="donate">
  <div class="section-mark"></div>
  <h2 class="section-title">Ways to Donate</h2>
  <svg class="divider" width="96" height="14" viewBox="0 0 96 14"><line x1="0" y1="7" x2="96" y2="7" stroke="#333" stroke-width="2"/><circle cx="48" cy="7" r="5" fill="#fff" stroke="#333" stroke-width="2"/></svg>
  <div class="card-row" style="top:275px">
    <article class="card">
      <div class="card-media" role="img" aria-label="Photo of memorial candles being lit" style="background:linear-gradient(135deg,#3a2e28,#b07a3c 60%,#e8c27a)"></div>
      <h3>Memorials &amp; Dedications</h3><div class="rule"></div>
      <p>Lorem ipsum dolor sit amet, consectetur adipisicing elit, sed do eiusmod tempor incididunt ut dolore.</p>
      <a class="card-go" href="#"><svg width="14" height="12" viewBox="0 0 14 12"><path d="M1 6 H12 M8 2 L12 6 L8 10" fill="none" stroke="#3f9a3a" stroke-width="2"/></svg></a>
    </article>
    <article class="card">
      <div class="card-media" role="img" aria-label="Photo of a senior couple planning with an advisor" style="background:linear-gradient(135deg,#e9eef2,#c9d3dc 50%,#d9b99a)"></div>
      <h3>Legacy &amp; Planned Giving</h3><div class="rule"></div>
      <p>Lorem ipsum dolor sit amet, consectetur adipisicing elit, sed do eiusmod tempor incididunt ut dolore.</p>
      <a class="card-go" href="#"><svg width="14" height="12" viewBox="0 0 14 12"><path d="M1 6 H12 M8 2 L12 6 L8 10" fill="none" stroke="#3f9a3a" stroke-width="2"/></svg></a>
    </article>
    <article class="card">
      <div class="card-media" role="img" aria-label="Photo of volunteers giving at work" style="background:linear-gradient(135deg,#5a3f3a,#3f8a8a 50%,#9a7a6a)"></div>
      <h3>Give at Work</h3><div class="rule"></div>
      <p>Lorem ipsum dolor sit amet, consectetur adipisicing elit, sed do eiusmod tempor incididunt ut dolore.</p>
      <a class="card-go" href="#"><svg width="14" height="12" viewBox="0 0 14 12"><path d="M1 6 H12 M8 2 L12 6 L8 10" fill="none" stroke="#3f9a3a" stroke-width="2"/></svg></a>
    </article>
  </div>
  <a class="btn see-more" href="#">SEE MORE WAYS &nbsp;→</a>
</section>

<section class="treatment">
  <div class="treatment-media" role="img" aria-label="Photo of a smiling doctor in blue scrubs holding a tablet"></div>
  <div class="treatment-body">
    <h2>OUR WAYS OF TREATMENT</h2>
    <h4>With latest technologies with other new treatment possibilities</h4>
    <p>Lorem ipsum dolor sit amet, consectetur adipisicing elit, sed do eiusmod tempor incididunt ut labore et dolore magna aliqua. Ut enim ad minim veniam, quis nostrud exercitation ullamco laboris nisi ut aliquip ex ea commodo consequat. Duis aute irure dolor in reprehenderit in voluptate velit esse cillum dolore eu fugiat nulla pariatur. Excepteur sint occaecat cupidatat non proident, sunt in culpa qui officia deserunt.</p>
    <a class="btn btn-read" href="#">READ MORE &nbsp;→</a>
  </div>
</section>

<section class="monthly">
  <h2>BECOME A MONTHLY DONOR</h2>
  <svg class="divider" width="96" height="14" viewBox="0 0 96 14"><line x1="0" y1="7" x2="96" y2="7" stroke="#fff" stroke-width="2"/><circle cx="48" cy="7" r="5" fill="#2d8b5e" stroke="#fff" stroke-width="2"/></svg>
  <p>Lorem ipsum dolor sit amet, consectetur adipisicing elit, sed do eiusmod tempor incididunt ut labore et dolore magna aliqua. Ut enim ad minim veniam, quis nostrud exercitation ullamco laboris nisi ut aliquip ex ea commodo consequat. Duis aute irure dolor in reprehenderit in voluptate velit esse cillum dolore eu fugiat nulla pariatur. Excepteur sint occaecat cupidatat non proident, sunt in culpa qui officia deserunt mollit anim id est laborum.</p>
  <a class="btn btn-ghost" href="#">DONATE NOW &nbsp;→</a>
</section>

<section class="interest">
  <h2 class="section-title">You May Also Be Interested In</h2>
  <svg class="divider" width="96" height="14" viewBox="0 0 96 14"><line x1="0" y1="7" x2="96" y2="7" stroke="#333" stroke-width="2"/><circle cx="48" cy="7" r="5" fill="#fff" stroke="#333" stroke-width="2"/></svg>
  <a class="slider-arrow" href="#" style="left:76px"><svg width="10" height="12" viewBox="0 0 10 12"><path d="M8 1 L2 6 L8 11" fill="none" stroke="#fff" stroke-width="2"/></svg></a>
  <a class="slider-arrow" href="#" style="left:1103px"><svg width="10" height="12" viewBox="0 0 10 12"><path d="M2 1 L8 6 L2 11" fill="none" stroke="#fff" stroke-width="2"/></svg></a>
  <div class="card-row">
    <article class="card">
      <div class="card-media" role="img" aria-label="Photo of a mother with her baby" style="background:linear-gradient(135deg,#5a3a2a,#a97a5a 50%,#e6d6c6)"></div>
      <h3>Headline Goes Here</h3><div class="rule"></div>
      <p>Lorem ipsum dolor sit amet, consectetur adipisicing elit, sed do eiusmod tempor incididunt ut dolore.</p>
      <a class="card-go" href="#"><svg width="14" height="12" viewBox="0 0 14 12"><path d="M1 6 H12 M8 2 L12 6 L8 10" fill="none" stroke="#3f9a3a" stroke-width="2"/></svg></a>
    </article>
    <article class="card">
      <div class="card-media" role="img" aria-label="Photo of a young child patient in a hospital" style="background:linear-gradient(135deg,#6a5a4a,#3f8a7a 55%,#c8c8c0)"></div>
      <h3>Headline Goes Here</h3><div class="rule"></div>
      <p>Lorem ipsum dolor sit amet, consectetur adipisicing elit, sed do eiusmod tempor incididunt ut dolore.</p>
      <a class="card-go" href="#"><svg width="14" height="12" viewBox="0 0 14 12"><path d="M1 6 H12 M8 2 L12 6 L8 10" fill="none" stroke="#3f9a3a" stroke-width="2"/></svg></a>
    </article>
    <article class="card">
      <div class="card-media" role="img" aria-label="Photo of clinicians treating a child patient" style="background:linear-gradient(135deg,#7aa6c0,#d8e2e8 50%,#c06a6a)"></div>
      <h3>Headline Goes Here</h3><div class="rule"></div>
      <p>Lorem ipsum dolor sit amet, consectetur adipisicing elit, sed do eiusmod tempor incididunt ut dolore.</p>
      <a class="card-go" href="#"><svg width="14" height="12" viewBox="0 0 14 12"><path d="M1 6 H12 M8 2 L12 6 L8 10" fill="none" stroke="#3f9a3a" stroke-width="2"/></svg></a>
    </article>
  </div>
</section>

<section class="cta-band">
  <a class="cta" href="#"><span class="cta-icon"><svg width="18" height="18" viewBox="0 0 18 18"><path d="M4 1 L7 1 L8 5 L6 7 C7 10 8 11 11 12 L13 10 L17 11 L17 14 C17 16 15 17 13 17 C6 16 2 12 1 5 C1 3 2 1 4 1Z" fill="#fff"/></svg></span><span class="cta-label">Call: 615.555.0182</span><svg class="arrow" width="14" height="12" viewBox="0 0 14 12"><path d="M1 6 H12 M8 2 L12 6 L8 10" fill="none" stroke="#fff" stroke-width="2"/></svg></a>
  <a class="cta" href="#"><span class="cta-icon"><svg width="20" height="14" viewBox="0 0 20 14"><rect x="1" y="1" width="18" height="12" fill="#fff"/><path d="M1 1 L10 8 L19 1" fill="none" stroke="#1b72b8" stroke-width="1.5"/></svg></span><span class="cta-label" style="font-size:13px">info@varrowickbr.com</span><svg class="arrow" width="14" height="12" viewBox="0 0 14 12"><path d="M1 6 H12 M8 2 L12 6 L8 10" fill="none" stroke="#fff" stroke-width="2"/></svg></a>
  <a class="cta" href="#"><span class="cta-icon"><svg width="20" height="18" viewBox="0 0 20 18"><path d="M10 17 C4 12 1 9 1 5.5 C1 3 3 1 5.5 1 C7.5 1 9 2.2 10 3.6 C11 2.2 12.5 1 14.5 1 C17 1 19 3 19 5.5 C19 9 16 12 10 17Z" fill="#fff"/></svg></span><span class="cta-label">Now Donate Us</span><svg class="arrow" width="14" height="12" viewBox="0 0 14 12"><path d="M1 6 H12 M8 2 L12 6 L8 10" fill="none" stroke="#fff" stroke-width="2"/></svg></a>
</section>

<footer class="site-footer">
  <div class="footer-col contact-col">
    <h5>Contact Us</h5>
    <div class="org">Varrowick Biomedical Research Institute</div>
    <div>48 Harlow Street, 6th Floor, New York,<br>NY 10014</div>
    <div style="margin-top:8px">
      <div class="line"><svg width="12" height="12" viewBox="0 0 18 18"><path d="M4 1 L7 1 L8 5 L6 7 C7 10 8 11 11 12 L13 10 L17 11 L17 14 C17 16 15 17 13 17 C6 16 2 12 1 5 C1 3 2 1 4 1Z" fill="#3f9a3a"/></svg>(800) 555-0147</div>
      <div class="line"><svg width="12" height="12" viewBox="0 0 12 12"><rect x="1" y="1" width="10" height="10" fill="#3f9a3a"/></svg>(212) 555-0193</div>
      <div class="line"><svg width="13" height="10" viewBox="0 0 20 14"><rect x="1" y="1" width="18" height="12" fill="#3f9a3a"/></svg>info@varrowickbr.com</div>
    </div>
  </div>
  <div class="footer-col nav-col">
    <h5>Navigation</h5>
    <ul>
      <li>› Home</li><li>› About Us</li><li>› Care &amp; Treatment</li><li>› Research</li><li>› Training</li><li>› Get Involved</li><li>› Contact Us</li>
    </ul>
  </div>
  <div class="footer-col sub-col">
    <h5>Subscribe Us</h5>
    <div class="sub-field"><span>Email Address</span><svg width="16" height="14" viewBox="0 0 16 14"><path d="M1 7 L15 1 L11 13 L8 8Z" fill="#3f9a3a"/></svg></div>
    <div class="socials"><span></span><span></span><span></span><span></span></div>
  </div>
  <div class="copyright">© Copyright 2017. Terms &amp; Conditions</div>
</footer>

</body>
</html>
```